Forest Consultant/Timber Buyer needs a clean business card

We are a forestry consulting and timber buying company. We meet with private landowners and assist them with timber management and timber harvesting. We would like a professional business card, please no clip art. logo is blue and white but would like to see a gray,silver, or some other color incorporated. Would like basic contact info. Would like to the layout to be creative and sleek but masculine.

Target Market(s)

private landowners

Industry/Entity Type

Business

Contact Information for Business Card

name,position, cell number, office number, email, website. This might be to cluttered. Basic contact info is what we are looking for.

Contact info can all be on one side with logo on the other.

Font styles to use
Serif
Sans Serif

Colors
0255a3
ffffff
aaaaaa

Requirements
Must have
• We just want it professional.
Nice to have
• Creative layout.
Should not have
• please no clip art of log trucks etc.

```html
<!DOCTYPE html>
<html lang="en">
<head>
<meta charset="utf-8">
<title>Oakline Timber – Business Card</title>
<link rel="stylesheet" href="https://fonts.googleapis.com/css2?family=Lato:wght@400;700;900&display=swap">
<style>
  :root {
    --stage: #2c2c2c;
    --card-white: #ffffff;
    --brand-blue: #17468f;
    --accent-green: #2aa83f;
    --text-light: #e6ecf5;
    --text-muted: #aab8d4;
  }
  * { margin: 0; padding: 0; box-sizing: border-box; }
  html, body {
    width: 1200px; height: 997px; overflow: hidden;
    background: var(--stage);
    font-family: "Lato", Arial, sans-serif;
  }
  .card {
    position: absolute;
    width: 520px; height: 300px;
    background: var(--card-white);
    overflow: hidden;
    box-shadow: 0 12px 30px rgba(0,0,0,.5);
  }
  .card--front { left: 90px; top: 130px; }
  .card--back  { left: 590px; top: 480px; }
  .card__band { position: absolute; inset: 0; width: 100%; height: 100%; }
  .wordmark {
    position: absolute;
    display: flex; align-items: center; gap: 12px;
  }
  .wordmark__dot {
    width: 38px; height: 38px; border-radius: 50%;
    background: var(--accent-green); flex: none;
  }
  .wordmark__name {
    color: var(--brand-blue);
    font-size: 28px; font-weight: 900; letter-spacing: .5px;
    white-space: nowrap;
  }
  .card--front .wordmark { left: 70px; top: 78px; }
  .card--back .wordmark { left: 60px; top: 48px; }
  .website {
    position: absolute; right: 40px; top: 188px;
    color: var(--text-light); font-size: 16px; font-weight: 700; letter-spacing: 2px;
  }
  .contact-list {
    position: absolute; right: 26px; top: 104px;
    list-style: none; text-align: right;
    color: var(--text-light); font-size: 13px; letter-spacing: .5px;
  }
  .contact-list li {
    display: flex; justify-content: flex-end; align-items: center; gap: 12px;
    height: 28px;
  }
  .contact-list svg { width: 14px; height: 14px; flex: none; }
  .person {
    position: absolute; left: 30px; top: 205px;
  }
  .person::before {
    content: ""; position: absolute; left: -30px; top: 26px;
    border-left: 14px solid var(--accent-green);
    border-top: 8px solid transparent; border-bottom: 8px solid transparent;
  }
  .person__name { color: var(--text-light); font-size: 22px; font-weight: 700; }
  .person__role { color: var(--text-muted); font-size: 17px; }
</style>
</head>
<body>

<section class="card card--front" aria-label="Business card front">
  <svg class="card__band" viewBox="0 0 520 300" preserveAspectRatio="none" aria-hidden="true">
    <path d="M0 232 Q300 222 520 62 L520 300 L0 300 Z" fill="var(--brand-blue)"/>
    <path d="M0 232 Q300 222 520 62" fill="none" stroke="var(--accent-green)" stroke-width="4"/>
  </svg>
  <div class="wordmark">
    <span class="wordmark__dot"></span>
    <span class="wordmark__name">Oakline Timber</span>
  </div>
  <p class="website">www.oaklinetimber.com</p>
</section>

<section class="card card--back" aria-label="Business card back">
  <svg class="card__band" viewBox="0 0 520 300" preserveAspectRatio="none" aria-hidden="true">
    <path d="M0 160 Q320 168 520 35 L520 300 L0 300 Z" fill="var(--brand-blue)"/>
    <path d="M0 160 Q320 168 520 35" fill="none" stroke="var(--accent-green)" stroke-width="4"/>
  </svg>
  <div class="wordmark">
    <span class="wordmark__dot"></span>
    <span class="wordmark__name">Oakline Timber</span>
  </div>
  <ul class="contact-list">
    <li>+852 5550 0142
      <svg viewBox="0 0 14 14" aria-hidden="true"><rect x="3.5" y="1" width="7" height="12" rx="1.2" fill="none" stroke="var(--text-muted)" stroke-width="1.3"/></svg>
    </li>
    <li>hello@oaklinetimber.com
      <svg viewBox="0 0 14 14" aria-hidden="true"><rect x="1" y="3" width="12" height="8" fill="var(--text-muted)"/><path d="M1 3 L7 8 L13 3" fill="none" stroke="var(--brand-blue)" stroke-width="1"/></svg>
    </li>
    <li>Harbor Court F12-14, Pine Bay
      <svg viewBox="0 0 14 14" aria-hidden="true"><path d="M7 13 C3 8 2.5 6.5 2.5 5 A4.5 4.5 0 0 1 11.5 5 C11.5 6.5 11 8 7 13 Z" fill="var(--text-muted)"/><circle cx="7" cy="5" r="1.6" fill="var(--brand-blue)"/></svg>
    </li>
  </ul>
  <div class="person">
    <p class="person__name">Daniel Hayes</p>
    <p class="person__role">Chief Executive Officer</p>
  </div>
</section>

</body>
</html>
```